Business Image

I have recently had a new company logo made up and require some new business cards to go with it.

Target Market(s)

Developers & high worth clients.

Industry/Entity Type

Business

Contact Information for Business Card

The business is in the construction/management industry. It needs to be classy but have a industrial feel. I would like the business card to be a elegant presentation in itself.

Requirements
Must have
• Current logo & company name. Colouring needs to be the same as the current design also.
Nice to have
• A few different designs & presentations of single and double sided business cards.

```html
<!DOCTYPE html>
<html lang="en">
<head>
<meta charset="utf-8">
<title>Keystone Build Group – Business Card</title>
<link rel="stylesheet" href="https://fonts.googleapis.com/css2?family=PT+Serif&family=Roboto:wght@400;500&display=swap">
<style>
  :root {
    --page-bg: #e9e6e1;
    --card-bg: #2e2e30;
    --card-bg-deep: #252527;
    --brand-blue: #62b4e2;
    --band-blue-light: #8fcbe8;
    --band-blue-dark: #4f9cc6;
    --contact-gold: #cbb99b;
    --text-light: #d6d6d6;
    --web-text: #2f4e60;
  }
  html, body {
    margin: 0;
    padding: 0;
    width: 1200px;
    height: 1010px;
    overflow: hidden;
    background: var(--page-bg);
  }
  .business-card {
    position: absolute;
    left: 100px;
    top: 215px;
    width: 1000px;
    height: 580px;
    background: linear-gradient(135deg, var(--card-bg) 0%, var(--card-bg-deep) 100%);
    overflow: hidden;
    box-shadow: 0 10px 30px rgba(0,0,0,0.18);
  }
  .brand {
    position: absolute;
    left: 66px;
    top: 96px;
    display: flex;
    align-items: center;
    gap: 26px;
  }
  .brand-square {
    width: 96px;
    height: 96px;
    background: var(--brand-blue);
  }
  .brand-name {
    font-family: "PT Serif", serif;
    font-size: 64px;
    line-height: 1;
    color: var(--brand-blue);
    letter-spacing: 0.5px;
  }
  .person {
    position: absolute;
    left: 66px;
    top: 418px;
  }
  .person-name {
    font-family: "PT Serif", serif;
    font-size: 36px;
    color: var(--brand-blue);
    line-height: 1.1;
  }
  .person-title {
    font-family: "Roboto", sans-serif;
    font-size: 21px;
    color: var(--text-light);
    margin-top: 4px;
  }
  .contact {
    position: absolute;
    left: 534px;
    top: 338px;
    font-family: "Roboto", sans-serif;
    color: var(--contact-gold);
  }
  .address {
    font-size: 23px;
    line-height: 32px;
    margin-bottom: 14px;
  }
  .contact-line {
    display: flex;
    align-items: center;
    gap: 20px;
    font-size: 23px;
    line-height: 34px;
  }
  .contact-line.email { color: var(--text-light); }
  .contact-icon { width: 22px; height: 18px; flex: none; }
  .footer-band {
    position: absolute;
    left: 0;
    bottom: 0;
    width: 1000px;
    height: 66px;
  }
  .website {
    position: absolute;
    left: 534px;
    bottom: 14px;
    font-family: "Roboto", sans-serif;
    font-size: 23px;
    color: var(--web-text);
  }
</style>
</head>
<body>
  <div class="business-card">
    <div class="brand">
      <div class="brand-square"></div>
      <div class="brand-name">Keystone Build Group</div>
    </div>

    <div class="person">
      <div class="person-name">John Smith</div>
      <div class="person-title">Director</div>
    </div>

    <div class="contact">
      <div class="address">123, Your city Name,<br>Street No. 113, Country 123456</div>
      <div class="contact-line phone">
        <svg class="contact-icon" viewBox="0 0 22 18" aria-hidden="true">
          <path d="M2 6 Q11 0 20 6 L18 8 L15 6 L15 4 Q11 3 7 4 L7 6 L4 8 Z" fill="#cbb99b"/>
          <rect x="5" y="9" width="12" height="8" rx="1.5" fill="#cbb99b"/>
        </svg>
        <span>000-1111-2222</span>
      </div>
      <div class="contact-line email">
        <svg class="contact-icon" viewBox="0 0 22 18" aria-hidden="true">
          <rect x="1" y="2" width="20" height="14" fill="#cbb99b"/>
          <path d="M1 2 L11 10 L21 2" fill="none" stroke="#2e2e30" stroke-width="1.6"/>
        </svg>
        <span>john@yourwebsite.com</span>
      </div>
    </div>

    <svg class="footer-band" viewBox="0 0 1000 66" aria-hidden="true">
      <defs>
        <linearGradient id="bandGradient" x1="0" y1="0" x2="1" y2="0">
          <stop offset="0" stop-color="#4f9cc6"/>
          <stop offset="0.5" stop-color="#8fcbe8"/>
          <stop offset="1" stop-color="#5aa8d3"/>
        </linearGradient>
      </defs>
      <polygon points="0,42 468,42 496,0 1000,0 1000,66 0,66" fill="url(#bandGradient)"/>
    </svg>
    <div class="website">www.yourwebsite.com</div>
  </div>
</body>
</html>
```